Ad designs for ChatterLoop and Vistapulse

We are a company that buy and sell airlines miles.
We publish our Ads on CL and Vistapulse and wish to receive 10 designs that reflects our business with some texts. Please see some examples.
10 designs with includes some text in English and those same 10 designs with include a text in Hebrew (written from right to left).
We need each of the designs to eventually be created at the following ratios and resolutions:
Square format (1:1): 1080 x 1080 pixels
Vertical format (9:16): 1080 x 1920 pixels
Horizontal format (16:9): 1280 x 720 pixels
Vertical video format (4:5): 1080 x 1350 pixels
Please see the samples sent and our login as well attached
Texts in English:
"We buy your airline miles for"
or
"Sell us your airline miles"
or
"Receive money for your airline miles"

and in Hebrew:
"אנחנו קונים את הנקודות שלכם בחברות התעופה"
or
"קונים נקודות נוסע מתמיד תמורת מזומן"
or
"קונים נקודות נתיב תכלת וחברות אחרות"

Please add a red button to all Ads in Eng saying "Get Quote"
and in Heb saying "להצעת מחיר"

```html
<!DOCTYPE html>
<html lang="en">
<head>
<meta charset="utf-8">
<title>Aerocash – airline miles ad set</title>
<link rel="stylesheet" href="https://fonts.googleapis.com/css2?family=Open+Sans:wght@700&family=Montserrat:wght@700;900&family=Heebo:wght@400;900&family=Allura&display=swap">
<style>
  :root{
    --panel-en:#8e8e8e;
    --panel-he:#777777;
    --label:#ffffff;
    --sky-top:#2aa6e0;
    --sky-mid:#8fd0f0;
    --sky-low:#f4fbff;
    --navy:#1c3aa6;
    --blue:#2d7ee0;
    --yellow:#ffe600;
    --red:#d81e1e;
    --ink:#1a1a1a;
    --scene-a:#f2f2f2;
    --scene-b:#b9c2c9;
    --scene-c:#f5d93a;
  }
  *{box-sizing:border-box;margin:0;padding:0}
  html,body{width:1200px;height:1200px;overflow:hidden}
  body{position:relative;font-family:"Montserrat",sans-serif}
  .panel{position:absolute;top:0;height:1200px;width:600px}
  .panel--en{left:0;background:var(--panel-en)}
  .panel--he{left:600px;background:var(--panel-he)}
  .panel-title{position:absolute;top:108px;font:700 38px "Open Sans",sans-serif;color:var(--label);width:600px;text-align:center}
  .panel--en .panel-title{left:-40px}
  .panel--he .panel-title{left:-28px}
  .size-label{position:absolute;font:700 18px "Open Sans",sans-serif;color:var(--label);transform:translateX(-50%);white-space:nowrap}

  .ad{position:absolute;overflow:hidden;
      background:linear-gradient(180deg,var(--sky-top) 0%,var(--sky-mid) 45%,var(--sky-low) 100%);
      box-shadow:0 2px 6px rgba(0,0,0,.25)}
  .ad-scene{position:absolute;border-radius:50% 50% 40% 40%;
      background:radial-gradient(ellipse at 55% 30%,var(--scene-a) 0%,var(--scene-b) 35%,transparent 62%),
                 radial-gradient(ellipse at 55% 72%,var(--scene-c) 0%,rgba(245,217,58,.55) 22%,transparent 48%)}
  .brand{position:absolute;display:flex;align-items:center;gap:4px;
      font:700 var(--bs,18px) "Montserrat",sans-serif;color:var(--ink);letter-spacing:.02em}
  .brand-mark{width:.8em;height:.8em;background:var(--ink)}
  .headline{position:absolute;font:900 var(--hs,20px)/1 "Montserrat",sans-serif;color:var(--navy);white-space:nowrap}
  .script{position:absolute;font:400 var(--ss,26px)/1 "Allura",cursive;color:var(--ink);white-space:nowrap}
  .band{position:absolute;background:var(--yellow);display:flex;flex-direction:column;justify-content:center;
      font:900 var(--ys,24px)/.95 "Montserrat",sans-serif;color:var(--blue);padding-left:6px;white-space:nowrap}
  .cta{position:absolute;background:var(--red);color:#fff;border-radius:8px;
      font:700 var(--cs,13px)/1 "Montserrat",sans-serif;padding:.6em .75em;white-space:nowrap}
  .cta::after{content:"";position:absolute;left:14%;bottom:-6px;border-left:4px solid transparent;border-right:4px solid transparent;border-top:7px solid var(--red)}

  .ad--he .headline,.ad--he .sub,.ad--he .band{direction:rtl;font-family:"Heebo",sans-serif;text-align:center}
  .ad--he .headline{font-weight:900;line-height:1}
  .sub{position:absolute;font:400 var(--us,16px)/1 "Heebo",sans-serif;color:var(--ink);white-space:nowrap}
  .ad--he .band{align-items:center;padding:0;font-weight:900;line-height:.9}
  .ad--he .cta{font-family:"Heebo",sans-serif;font-weight:700}
  .center{left:50%;transform:translateX(-50%)}
</style>
</head>
<body>

<section class="panel panel--en">
  <h2 class="panel-title">English version</h2>

  <span class="size-label" style="left:136px;top:403px">1080x1920</span>
  <article class="ad ad--en" style="left:49px;top:437px;width:246px;height:438px">
    <div class="ad-scene" role="img" aria-label="Airplane at an aircraft window with a smiling traveller on a yellow suitcase holding cash" style="left:10%;top:14%;width:80%;height:52%"></div>
    <div class="brand center" style="top:7%;--bs:19px"><span>AEROCASH</span><span class="brand-mark"></span></div>
    <div class="headline center" style="top:65%;--hs:19px">RECEIVE MONEY</div>
    <div class="script center" style="top:69%;--ss:26px">for your</div>
    <div class="band" style="left:11%;top:76%;width:78%;height:8%;--ys:22px;align-items:center;padding:0">AIRLINE MILES</div>
    <div class="cta center" style="top:86%;--cs:12px">Get Quote</div>
  </article>

  <span class="size-label" style="left:422px;top:226px">1080x1350</span>
  <article class="ad ad--en" style="left:307px;top:259px;width:246px;height:307px">
    <div class="ad-scene" role="img" aria-label="Airplane at an aircraft window with a smiling traveller on a yellow suitcase holding cash" style="left:44%;top:4%;width:60%;height:96%"></div>
    <div class="brand" style="left:11%;top:10%;--bs:17px"><span>AEROCASH</span><span class="brand-mark"></span></div>
    <div class="headline" style="left:9%;top:23%;--hs:20px">RECEIVE<br>MONEY</div>
    <div class="script" style="left:10%;top:37%;--ss:28px">for your</div>
    <div class="band" style="left:8%;top:48%;width:58%;height:17%;--ys:23px">AIRLINE<br>MILES</div>
    <div class="cta" style="left:10%;top:77%;--cs:12px">Get Quote</div>
  </article>

  <span class="size-label" style="left:430px;top:849px">1080x1080</span>
  <article class="ad ad--en" style="left:307px;top:579px;width:246px;height:246px">
    <div class="ad-scene" role="img" aria-label="Airplane at an aircraft window with a smiling traveller on a yellow suitcase holding cash" style="left:46%;top:4%;width:58%;height:96%"></div>
    <div class="brand" style="left:11%;top:9%;--bs:16px"><span>AEROCASH</span><span class="brand-mark"></span></div>
    <div class="headline" style="left:11%;top:25%;--hs:18px">RECEIVE<br>MONEY</div>
    <div class="script" style="left:11%;top:42%;--ss:24px">for your</div>
    <div class="band" style="left:10%;top:57%;width:58%;height:20%;--ys:21px">AIRLINE<br>MILES</div>
    <div class="cta" style="left:11%;top:80%;--cs:10px">Get Quote</div>
  </article>

  <span class="size-label" style="left:159px;top:1067px">1280 x 720</span>
  <article class="ad ad--en" style="left:47px;top:887px;width:292px;height:165px">
    <div class="ad-scene" role="img" aria-label="Airplane at an aircraft window with a smiling traveller on a yellow suitcase holding cash" style="left:62%;top:2%;width:40%;height:98%"></div>
    <div class="brand" style="left:9%;top:12%;--bs:14px"><span>AEROCASH</span><span class="brand-mark"></span></div>
    <div class="headline" style="left:9%;top:31%;--hs:15px">RECEIVE MONEY</div>
    <div class="script" style="left:10%;top:42%;--ss:20px">for your</div>
    <div class="band" style="left:9%;top:55%;width:66%;height:14%;--ys:17px">AIRLINE MILES</div>
    <div class="cta" style="left:10%;top:76%;--cs:8px">Get Quote</div>
  </article>
</section>

<section class="panel panel--he">
  <h2 class="panel-title">Hebrew version</h2>

  <span class="size-label" style="left:161px;top:403px">1080x1920</span>
  <article class="ad ad--he" lang="he" style="left:40px;top:432px;width:263px;height:466px">
    <div class="ad-scene" role="img" aria-label="Airplane at an aircraft window with a smiling traveller on a yellow suitcase holding cash" style="left:10%;top:13%;width:80%;height:52%"></div>
    <div class="brand center" style="top:6%;--bs:20px"><span>AEROCASH</span><span class="brand-mark"></span></div>
    <div class="headline center" style="top:62%;--hs:17px">אנחנו<br>קונים את</div>
    <div class="sub center" style="top:69.6%;--us:15px">הנקודות שלכם</div>
    <div class="band" style="left:19%;top:73.8%;width:63%;height:9.2%;--ys:20px">בחברות<br>התעופה</div>
    <div class="cta center" style="top:85.5%;--cs:10px">קבל הצעת מחיר</div>
  </article>

  <span class="size-label" style="left:446px;top:226px">1080x1350</span>
  <article class="ad ad--he" lang="he" style="left:315px;top:259px;width:263px;height:328px">
    <div class="ad-scene" role="img" aria-label="Airplane at an aircraft window with a smiling traveller on a yellow suitcase holding cash" style="left:44%;top:6%;width:60%;height:94%"></div>
    <div class="brand" style="left:13%;top:14%;--bs:20px"><span>AEROCASH</span><span class="brand-mark"></span></div>
    <div class="headline" style="left:10%;top:33%;width:36%;--hs:20px">אנחנו<br>קונים את</div>
    <div class="sub" style="left:10%;top:47%;--us:16px;direction:rtl">הנקודות שלכם</div>
    <div class="band" style="left:9%;top:57%;width:48%;height:13%;--ys:21px">בחברות<br>התעופה</div>
    <div class="cta" style="left:11%;top:80%;--cs:10px">להצעת מחיר</div>
  </article>

  <span class="size-label" style="left:455px;top:884px">1080x1080</span>
  <article class="ad ad--he" lang="he" style="left:315px;top:602px;width:263px;height:263px">
    <div class="ad-scene" role="img" aria-label="Airplane at an aircraft window with a smiling traveller on a yellow suitcase holding cash" style="left:46%;top:8%;width:58%;height:92%"></div>
    <div class="brand" style="left:14%;top:12%;--bs:17px"><span>AEROCASH</span><span class="brand-mark"></span></div>
    <div class="headline" style="left:12%;top:30%;width:34%;--hs:17px">אנחנו<br>קונים את</div>
    <div class="sub" style="left:15%;top:46%;--us:14px;direction:rtl">הנקודות שלכם</div>
    <div class="band" style="left:12%;top:57%;width:45%;height:16%;--ys:18px">בחברות<br>התעופה</div>
    <div class="cta" style="left:13%;top:80%;--cs:9px">להצעת מחיר</div>
  </article>

  <span class="size-label" style="left:197px;top:1105px">1280 x 720</span>
  <article class="ad ad--he" lang="he" style="left:42px;top:912px;width:311px;height:174px">
    <div class="ad-scene" role="img" aria-label="Airplane at an aircraft window with a smiling traveller on a yellow suitcase holding cash" style="left:56%;top:4%;width:46%;height:96%"></div>
    <div class="brand" style="left:19%;top:12%;--bs:14px"><span>AEROCASH</span><span class="brand-mark"></span></div>
    <div class="headline" style="left:14%;top:29%;width:32%;--hs:13px">אנחנו<br>קונים את</div>
    <div class="sub" style="left:16%;top:45%;--us:11px;direction:rtl">הנקודות שלכם</div>
    <div class="band" style="left:14%;top:55%;width:51%;height:17%;--ys:14px">בחברות<br>התעופה</div>
    <div class="cta" style="left:19%;top:76%;--cs:7px">קבל הצעת מחיר</div>
  </article>
</section>

</body>
</html>
```